Comprehensive Branding Development for Brightwater Holdings Limited

We have our logo and are seeking a talented graphic designer to help us develop a cohesive branding guideline based on this logo provided by our client.
The goal is to create a comprehensive branding package for various office stationery items and promotional materials.

Deliverables:

The designer will be responsible for creating branding guidelines for the following items:

Letterhead
Envelope
Business card
Key holders
T-shirts
Face cap
Car branding
Pen
Dangler (Air Fresheners)
Lapel pin
PowerPoint template
ID card
Carrier bag
Notebook
Mug cup
Umbrella

Logo Text

Logo Provided by client and no needs for designing a new logo

```html
<!DOCTYPE html>
<html lang="en">
<head>
<meta charset="utf-8">
<title>Brightwater Holdings Limited – Mouse Pad</title>
<link rel="stylesheet" href="https://fonts.googleapis.com/css2?family=Open+Sans:wght@400;600&display=swap">
<style>
  :root {
    --backdrop: #dedede;
    --pad-white: #f4f4f4;
    --pad-light: #e9e9e9;
    --band-grey: #d2d2d2;
    --charcoal: #3b393c;
    --brand-red: #e2282c;
    --text-grey: #8a8a8a;
  }
  html, body {
    margin: 0;
    padding: 0;
    width: 1200px;
    height: 900px;
    overflow: hidden;
    background: var(--backdrop);
    font-family: "Open Sans", Arial, sans-serif;
  }
  .mouse-pad {
    position: absolute;
    left: 100px;
    top: 90px;
    width: 1000px;
    height: 720px;
  }
  .brand-block {
    position: absolute;
    left: 70px;
    top: 70px;
    display: flex;
    align-items: flex-start;
    gap: 12px;
  }
  .brand-square {
    width: 22px;
    height: 22px;
    background: var(--brand-red);
    margin-top: 3px;
  }
  .brand-name {
    margin: 0;
    font-size: 21px;
    font-weight: 600;
    color: var(--brand-red);
    letter-spacing: 0.5px;
    line-height: 1.2;
  }
  .brand-tagline {
    margin: 4px 0 0;
    font-size: 10px;
    color: var(--text-grey);
    letter-spacing: 0.5px;
  }
  .brand-services {
    margin: 6px 0 0;
    font-size: 9px;
    color: var(--brand-red);
    letter-spacing: 0.3px;
  }
  .corner-name {
    position: absolute;
    right: 48px;
    bottom: 44px;
    margin: 0;
    font-size: 15px;
    font-weight: 600;
    color: var(--pad-white);
    letter-spacing: 0.5px;
  }
</style>
</head>
<body>
  <div class="mouse-pad">
    <svg width="1000" height="720" viewBox="0 0 1000 720">
      <defs>
        <clipPath id="pad-shape">
          <rect x="0" y="0" width="1000" height="720" rx="64" ry="64"/>
        </clipPath>
        <linearGradient id="band-fade" x1="0" y1="0" x2="0" y2="1">
          <stop offset="0" stop-color="var(--pad-light)"/>
          <stop offset="1" stop-color="var(--band-grey)"/>
        </linearGradient>
      </defs>
      <g clip-path="url(#pad-shape)">
        <rect class="pad-base" x="0" y="0" width="1000" height="720" fill="var(--pad-white)"/>
        <rect class="pad-soft-band" x="200" y="0" width="170" height="720" fill="var(--pad-light)"/>
        <rect class="pad-halftone-band" x="370" y="0" width="110" height="720" fill="url(#band-fade)" role="img" aria-label="Vertical band of halftone dots fading in grey"/>
        <polygon class="dark-panel" fill="var(--charcoal)"
          points="560,720 560,500 760,500 760,300 850,300 850,70 1000,70 1000,720"/>
        <rect class="red-bar red-bar-main" x="640" y="300" width="82" height="370" fill="var(--brand-red)"/>
        <rect class="red-bar red-bar-side" x="880" y="220" width="56" height="200" fill="var(--brand-red)"/>
        <g class="accent-lines" stroke="var(--brand-red)" stroke-width="2" fill="none">
          <line x1="600" y1="390" x2="600" y2="620"/>
          <line x1="800" y1="40" x2="800" y2="280"/>
          <line x1="950" y1="110" x2="950" y2="210"/>
          <line x1="770" y1="360" x2="770" y2="470"/>
          <polyline points="580,720 580,530 790,530 790,460 960,460"/>
        </g>
      </g>
    </svg>

    <div class="brand-block">
      <div class="brand-square"></div>
      <div>
        <p class="brand-name">Brightwater Holdings Limited</p>
        <p class="brand-tagline">Investment Advisory</p>
        <p class="brand-services">Wealth Management · Asset Management</p>
      </div>
    </div>

    <p class="corner-name">Brightwater</p>
  </div>
</body>
</html>
```